CloudRiver Business Card

I need something that flows with the logo and looks professional but creative. I included the thumbnail file of the photo but will upload the source file once I have it. Colors of business card should flow. I am interested in doing the translucent clear plastic cards as well. My company is called CloudRiver in one word and the contact details are below:

Dale Hollings
555-318-4720
www.CloudRiverTx.example
dhollings_47@mailbox.example
Updates

Too much red. I'd rather focus on the blue and put some silver or grey in there.

New Files uploaded. Like the designs so far and am looking forward to seeing more.

Looking for a whole new direction. Let's forget about the plastic card. Let's focus on the blue more than red. I still haven't seen something that really grabs me.

Industry/Entity Type

Plastic

```html
<!DOCTYPE html>
<html lang="en">
<head>
<meta charset="utf-8">
<title>CloudRiver Business Card</title>
<link rel="stylesheet" href="https://fonts.googleapis.com/css2?family=Arimo:ital,wght@0,400;0,700;1,700&display=swap">
<style>
  :root {
    --backdrop: #2a2433;
    --card-black: #050505;
    --brand-red: #e3141f;
    --brand-blue: #1f7fc4;
    --art-blue: #1a5f96;
    --art-grey: #3a3d42;
    --silver-light: #f1f1f1;
    --silver-mid: #d4d4d4;
    --silver-dark: #b9b9b9;
  }
  * { margin: 0; padding: 0; box-sizing: border-box; }
  html, body {
    width: 1200px;
    height: 800px;
    overflow: hidden;
    background: var(--backdrop);
    font-family: "Arimo", Arial, sans-serif;
  }
  .card-sheet {
    position: relative;
    width: 1200px;
    height: 800px;
    display: flex;
    align-items: center;
    justify-content: center;
    gap: 40px;
  }
  .card {
    position: relative;
    width: 540px;
    height: 310px;
    overflow: hidden;
  }
  .card-front { background: var(--card-black); }
  .card-back {
    background: linear-gradient(135deg, var(--silver-light) 0%, var(--silver-mid) 55%, var(--silver-dark) 100%);
  }
  .corner-art {
    position: absolute;
    left: 0;
    top: 24px;
    width: 190px;
    height: 78px;
    background: linear-gradient(90deg, var(--art-blue) 0%, var(--art-grey) 100%);
    opacity: 0.85;
  }
  .contact-block {
    position: absolute;
    left: 96px;
    top: 116px;
    line-height: 1.22;
  }
  .contact-name {
    color: var(--brand-red);
    font-weight: 700;
    font-style: italic;
    font-size: 21px;
    margin-bottom: 2px;
  }
  .contact-line {
    color: var(--brand-blue);
    font-size: 18px;
    font-weight: 400;
  }
  .brand-name {
    color: var(--brand-blue);
    font-weight: 700;
    font-size: 42px;
    letter-spacing: 0.5px;
    white-space: nowrap;
  }
  .card-front .brand-name {
    position: absolute;
    right: 40px;
    bottom: 40px;
  }
  .card-back .brand-name {
    position: absolute;
    left: 50%;
    top: 50%;
    transform: translate(-50%, -50%);
    font-size: 48px;
  }
</style>
</head>
<body>
  <main class="card-sheet">
    <section class="card card-front">
      <div class="corner-art" role="img" aria-label="Illustration of a vapour device with rising vapour"></div>
      <div class="contact-block">
        <p class="contact-name">Dale Hollings</p>
        <p class="contact-line">555-318-4720</p>
        <p class="contact-line">www.CloudRiverTx.example</p>
        <p class="contact-line">dhollings_47@mailbox.example</p>
      </div>
      <p class="brand-name">CloudRiver</p>
    </section>
    <section class="card card-back">
      <p class="brand-name">CloudRiver</p>
    </section>
  </main>
</body>
</html>
```